Project Transparent, Clean, and Simple.

Please use the current website for any materials: www.venholdrusk.com - I don't have anything that I can upload - sorry :)

To clarify we want to create pages for each tab on the existing site. If you think there is a better way to group these or showcase these categories please feel free to do so but please include these pages.

1.Home Page
Your Needs should each have a separate page
2. Family Office
3. Entrepreneurs
4.Open Fiduciary
5. Your Team
6. Insights
7. News & Media
8. Contact Us

We just want this site to look like Quiller.com. Simple. Easy. Impactful.
Current website again is:
https://www.venholdrusk.com/

We are doing something completely different from everyone else in our industry, and we want people to realize that this is not an ordinary place. We want to bring transparency to our clients, make them feel comfortable and gain trust in our beliefs. We provide everything from doing your taxes, travel planning, financial planning, estate planning, legal work, family and life management issues - etc. Our main service is managing money but with the obligation of providing our clients options that have their best interests in mind - which most banks cannot and do not do.

If our site does not show that we are simple, transparent, and easy to use. We won't be able to get that far. It also needs to be easy enough to view videos and for people to sign up to learn more without being in front of your face as the main call to action.

Target Market(s)

Entrepreneurs and High Net Worth Individuals

Industry/Entity Type

Financial Service

Number of Pages Required

5+ page

Font styles to use
Sans Serif
Other font styles liked:
• Times New Roman, Palatino, Georgia, Courier, Bookman and Garamond

Colors
1b1b1b
ffffff
0292cd

Requirements
Must have
• Simple. A lot of White Space. Needs to look as simple and impactful as Quiller.com.
Nice to have
• White Space
Should not have
• A lot of colors. Not much White Space. Busy.

```html
<!DOCTYPE html>
<html lang="en">
<head>
<meta charset="utf-8">
<title>Venhold Rusk — Candid Family Wealth Partners</title>
<link href="https://fonts.googleapis.com/css2?family=Open+Sans:wght@300;400;600;700&display=swap" rel="stylesheet">
<style>
:root{
  --ink:#1b1b1b;
  --white:#ffffff;
  --blue:#0b5ea8;
  --tile-blue:#0a55a6;
  --text:#333333;
  --muted:#777777;
  --line:#e3e3e3;
  --tile-grey:#eeeeee;
  --tile-light:#f6f6f6;
  --footer:#f2f2f2;
}
*{box-sizing:border-box;margin:0;padding:0}
html,body{width:1200px;height:2459px;overflow:hidden}
body{font-family:"Open Sans",Arial,sans-serif;color:var(--text);background:var(--white);position:relative}

/* Nav */
.site-nav{position:absolute;left:0;top:0;width:1200px;height:74px;background:var(--ink)}
.brand{position:absolute;left:161px;top:21px;color:var(--white)}
.brand-name{display:flex;align-items:center;font-size:18px;font-weight:700;letter-spacing:-.2px;line-height:22px}
.brand-name i{display:inline-block;width:13px;height:13px;background:#9aa3ad;margin-right:5px}
.brand-tag{font-size:8.5px;color:#bbb;line-height:12px}
.menu{position:absolute;top:0;left:0;width:1200px;height:74px;font-size:12px;color:var(--white)}
.menu span{position:absolute;top:30px;display:flex;align-items:center;white-space:nowrap}
.menu .caret{width:0;height:0;border-left:4px solid transparent;border-right:4px solid transparent;border-top:5px solid #fff;margin-left:6px}

/* Hero */
.hero{position:absolute;left:0;top:74px;width:1200px;height:560px;
  background:radial-gradient(circle at 600px 330px,#5da6d6 0,#2b5d8a 90px,#1a3050 200px,rgba(16,24,40,0) 320px),
  linear-gradient(90deg,#151b26 0,#2a3a56 40%,#1d2a44 70%,#0f1522 100%)}
.hero h1{position:absolute;top:30px;width:100%;text-align:center;color:var(--white);font-weight:300;font-size:45px}
.hero .sub{position:absolute;top:97px;width:100%;text-align:center;color:#e8eef6;font-weight:300;font-size:24px}
.hero .cta{position:absolute;left:523px;top:152px;width:152px;height:36px;border:2px solid #fff;border-radius:18px;color:#fff;font-size:14px;line-height:32px;text-align:center}
.dots{position:absolute;top:516px;left:570px;display:flex}
.dots i{width:10px;height:10px;border-radius:50%;background:#aab3bf;margin-right:5px}
.dots i:first-child{background:#fff}

/* Numbers */
.section-title{position:absolute;width:100%;text-align:center;font-weight:300;font-size:31px;color:var(--ink)}
.stats{position:absolute;left:145px;top:725px;display:flex}
.stat{width:102px;text-align:center}
.stat b{display:block;font-size:35px;font-weight:700;color:var(--ink);line-height:44px}
.stat span{display:block;font-size:11px;color:var(--muted);line-height:18px;margin-top:6px}
.rule{position:absolute;left:0;width:1200px;height:1px;background:var(--line)}

/* Services */
.service{position:absolute;width:230px}
.service svg{position:absolute;left:-74px;top:-2px}
.service h3{font-size:17px;font-weight:400;color:var(--blue);line-height:22px;white-space:nowrap}
.service p{font-size:10.5px;color:var(--muted);line-height:20px;margin-top:8px;white-space:nowrap}

/* Fiduciary */
.fiduciary{position:absolute;left:0;top:1382px;width:1200px;height:414px;
  background:radial-gradient(ellipse at 1050px 60px,#2a4a22 0,rgba(30,40,25,0) 320px),linear-gradient(90deg,#3a3428 0,#4a4230 40%,#2f3426 70%,#1e2a1c 100%)}
.fiduciary h2{position:absolute;top:42px;width:100%;text-align:center;color:#fff;font-weight:300;font-size:31px}
.fiduciary h4{position:absolute;left:160px;top:118px;color:#fff;font-weight:400;font-size:18.5px}
.fiduciary p{position:absolute;left:160px;width:485px;color:#eee;font-size:10.8px;line-height:19.5px}
.video{position:absolute;left:698px;top:129px;width:346px;height:210px;background:#8d8d8d;padding:6px}
.video .screen{width:100%;height:180px;background:linear-gradient(180deg,#dcdcdc,#c8c8c8)}
.video .bar{position:absolute;left:6px;bottom:6px;width:334px;height:18px;background:#3b3b3b}
.video .bar i{position:absolute;left:20px;top:8px;width:230px;height:3px;background:#999}
.play{position:absolute;left:168px;top:76px;width:40px;height:40px;border-radius:50%;background:rgba(60,60,60,.6)}
.play:after{content:"";position:absolute;left:15px;top:11px;border-left:14px solid #fff;border-top:9px solid transparent;border-bottom:9px solid transparent}

/* Tiles */
.tiles{position:absolute;left:0;top:1796px;width:1200px;height:212px;display:flex}
.tile{width:300px;height:212px;padding:56px 0 0 20px;background:var(--tile-grey)}
.tile:nth-child(1){background:var(--tile-blue);color:#fff}
.tile:nth-child(3){background:var(--tile-light)}
.tile h3{font-size:22px;font-weight:300;color:#333;display:flex;align-items:center}
.tile:nth-child(1) h3{color:#fff}
.tile h3 svg{margin-right:8px}
.tile p{font-size:10.5px;line-height:19px;margin-top:22px;color:#555;width:265px}
.tile:nth-child(1) p{color:#fff}

/* Press */
.press{position:absolute;left:160px;top:2062px;width:880px;display:flex;justify-content:space-between;font-size:22px;font-weight:700;color:#b5b5b5}

/* Footer */
.footer{position:absolute;left:0;top:2147px;width:1200px;height:312px;background:var(--footer);border-top:1px solid var(--line)}
.footer .brand{top:40px;left:161px;color:#333}
.footer .brand-tag{color:#777}
.footer .about{position:absolute;left:160px;top:102px;width:215px;font-size:10px;line-height:19px;color:#666}
.fcol{position:absolute;top:40px;font-size:10px;color:#666;line-height:21px}
.fcol h5{font-size:13.5px;font-weight:400;color:#333;margin-bottom:12px}
.footer .baseline{position:absolute;left:160px;top:246px;width:880px;height:1px;background:#ddd}
.copy{position:absolute;left:160px;top:272px;font-size:10px;color:#333}
.social{position:absolute;left:914px;top:264px;display:flex}
.social i{width:26px;height:26px;border-radius:50%;margin-right:6px}
</style>
</head>
<body>

<header class="site-nav">
  <div class="brand">
    <div class="brand-name"><i></i>VenholdRusk</div>
    <div class="brand-tag">Candid Family Wealth Partners</div>
  </div>
  <nav class="menu">
    <span style="left:518px">Home</span>
    <span style="left:587px">Your Needs<i class="caret"></i></span>
    <span style="left:683px">Your Team</span>
    <span style="left:775px">Insights</span>
    <span style="left:854px">News and Media<i class="caret"></i></span>
    <span style="left:980px">Contact Us</span>
  </nav>
</header>

<section class="hero" role="img" aria-label="Photo of an open hand holding a glowing globe wrapped in network lines, dark blue background">
  <h1>Venhold Rusk</h1>
  <div class="sub">Candid Family Wealth Partners</div>
  <div class="cta">Get Started Here</div>
  <div class="dots"><i></i><i></i><i></i><i></i></div>
</section>

<h2 class="section-title" style="top:656px">Our Numbers</h2>
<div class="stats">
  <div class="stat"><b>99%</b><span>Client<br>Retention<br>Since</span></div>
  <div class="stat"><b>30</b><span>Ledgerline #30<br>Advisor 2016</span></div>
  <div class="stat"><b>67</b><span>Marlow's #67<br>Advisor 2016</span></div>
  <div class="stat"><b>$2.5B</b><span>Assets Under<br>Advisory</span></div>
  <div class="stat"><b>21</b><span>Awards<br>Received</span></div>
  <div class="stat"><b>70</b><span># Of Business<br>Liquidity<br>Events</span></div>
  <div class="stat"><b>23</b><span>Family Office<br>Staff</span></div>
  <div class="stat"><b>2</b><span># 2 Advisor In<br>Virginia</span></div>
  <div class="stat"><b>20</b><span>National TV<br>Spots</span></div>
</div>
<div class="rule" style="top:859px"></div>

<h2 class="section-title" style="top:882px">Our Services</h2>

<div class="service" style="left:234px;top:962px">
  <svg width="56" height="40" viewBox="0 0 56 40"><circle cx="24" cy="22" r="15" fill="none" stroke="#0b5ea8" stroke-width="3"/><path d="M4 18 L50 8 L54 12 L30 22 L22 36 L17 35 L20 24 L8 26 Z" fill="#0b5ea8"/></svg>
  <h3>Travel Planning</h3>
  <p>Sed ut perspiciatis unde omnis iste natus sit<br>voluptatem accusantium doloremque laudan<br>tium, totamrem aperiame ips.</p>
</div>
<div class="service" style="left:539px;top:962px">
  <svg width="50" height="40" viewBox="0 0 50 40"><rect x="6" y="26" width="6" height="12" fill="#0b5ea8"/><rect x="15" y="20" width="6" height="18" fill="#0b5ea8"/><rect x="24" y="14" width="6" height="24" fill="#0b5ea8"/><rect x="33" y="8" width="6" height="30" fill="#0b5ea8"/><path d="M4 20 L18 10 L26 14 L40 2" stroke="#0b5ea8" stroke-width="2.5" fill="none"/></svg>
  <h3>Investment Strategy</h3>
  <p>Sed ut perspiciatis unde omnis iste natus sit<br>voluptatem accusantium doloremque laudan<br>tium, totamrem aperiame ips.</p>
</div>
<div class="service" style="left:844px;top:962px">
  <svg width="50" height="40" viewBox="0 0 50 40"><path d="M4 16 L24 3 L44 16 Z" fill="#0b5ea8"/><rect x="6" y="16" width="36" height="20" fill="#0b5ea8"/><rect x="12" y="21" width="6" height="6" fill="#fff"/><rect x="30" y="21" width="6" height="6" fill="#fff"/><rect x="21" y="24" width="6" height="12" fill="#fff"/></svg>
  <h3>Estate Planning</h3>
  <p>Sed ut perspiciatis unde omnis iste natus sit<br>voluptatem accusantium doloremque laudan<br>tium, totamrem aperiame ips.</p>
</div>

<div class="service" style="left:234px;top:1098px">
  <svg width="50" height="40" viewBox="0 0 50 40"><rect x="23" y="2" width="3" height="32" fill="#0b5ea8"/><rect x="14" y="34" width="21" height="4" fill="#0b5ea8"/><rect x="6" y="6" width="37" height="3" fill="#0b5ea8"/><path d="M3 22 L10 9 L17 22 Z M32 22 L39 9 L46 22 Z" fill="none" stroke="#0b5ea8" stroke-width="2"/><path d="M3 22 A7 5 0 0 0 17 22 Z M32 22 A7 5 0 0 0 46 22 Z" fill="#0b5ea8"/></svg>
  <h3>Legal Advisory</h3>
  <p>Sed ut perspiciatis unde omnis iste natus sit<br>voluptatem accusantium doloremque laudan<br>tium, totamrem aperiame ips.</p>
</div>
<div class="service" style="left:539px;top:1098px">
  <svg width="50" height="40" viewBox="0 0 50 40"><circle cx="14" cy="10" r="7" fill="#0b5ea8"/><circle cx="34" cy="10" r="7" fill="#0b5ea8"/><path d="M2 36 Q2 20 14 20 Q26 20 26 36 Z M22 36 Q22 20 34 20 Q46 20 46 36 Z" fill="#0b5ea8"/></svg>
  <h3>Family</h3>
  <p>Sed ut perspiciatis unde omnis iste natus sit<br>voluptatem accusantium doloremque laudan<br>tium, totamrem aperiame ips.</p>
</div>
<div class="service" style="left:844px;top:1098px">
  <svg width="50" height="40" viewBox="0 0 50 40"><rect x="4" y="5" width="24" height="30" rx="2" fill="none" stroke="#0b5ea8" stroke-width="3"/><rect x="10" y="2" width="12" height="6" fill="#0b5ea8"/><path d="M9 18 L13 22 L21 13" stroke="#0b5ea8" stroke-width="2.5" fill="none"/><circle cx="32" cy="28" r="10" fill="#fff" stroke="#0b5ea8" stroke-width="3"/><path d="M32 22 V28 H37" stroke="#0b5ea8" stroke-width="2" fill="none"/></svg>
  <h3>Life management issues</h3>
  <p>Sed ut perspiciatis unde omnis iste natus sit<br>voluptatem accusantium doloremque laudan<br>tium, totamrem aperiame ips.</p>
</div>

<div class="service" style="left:234px;top:1235px">
  <svg width="50" height="40" viewBox="0 0 50 40"><circle cx="10" cy="10" r="8" fill="#0b5ea8"/><path d="M18 10 H28 M28 10 L36 4 M28 10 L36 18 M28 10 V30" stroke="#0b5ea8" stroke-width="2.5"/><circle cx="38" cy="4" r="3" fill="#0b5ea8"/><circle cx="38" cy="18" r="3" fill="#0b5ea8"/><rect x="22" y="30" width="12" height="8" fill="#0b5ea8"/></svg>
  <h3>Cashflow Management</h3>
  <p>Sed ut perspiciatis unde omnis iste natus sit<br>voluptatem accusantium doloremque laudan<br>tium, totamrem aperiame ips.</p>
</div>
<div class="service" style="left:539px;top:1235px">
  <svg width="50" height="40" viewBox="0 0 50 40"><rect x="4" y="2" width="26" height="34" rx="2" fill="none" stroke="#0b5ea8" stroke-width="3"/><path d="M9 12 H24 M9 19 H22 M9 26 H18" stroke="#0b5ea8" stroke-width="2"/><circle cx="32" cy="26" r="9" fill="#fff" stroke="#0b5ea8" stroke-width="2.5"/><path d="M32 21 V31" stroke="#0b5ea8" stroke-width="2"/></svg>
  <h3>Tax Minimization</h3>
  <p>Sed ut perspiciatis unde omnis iste natus sit<br>voluptatem accusantium doloremque laudan<br>tium, totamrem aperiame ips.</p>
</div>
<div class="service" style="left:844px;top:1235px">
  <svg width="50" height="40" viewBox="0 0 50 40"><rect x="10" y="2" width="32" height="18" fill="none" stroke="#0b5ea8" stroke-width="3"/><circle cx="26" cy="11" r="4" fill="#0b5ea8"/><path d="M2 28 Q10 22 20 26 L30 26 Q34 28 30 30 L18 30 L34 32 L46 24 Q48 28 44 32 L30 38 L2 38 Z" fill="#0b5ea8"/></svg>
  <h3>Philanthropy</h3>
  <p>Sed ut perspiciatis unde omnis iste natus sit<br>voluptatem accusantium doloremque laudan<br>tium, totamrem aperiame ips.</p>
</div>

<section class="fiduciary" role="img" aria-label="Blurred warm-toned photo background behind the fiduciary section">
  <h2>What is an Open Fiduciary?</h2>
  <h4>Financial advisor who acts in the interests of their clients</h4>
  <p style="top:172px">Worried about the financial advisor charged with protecting your hard-earned wealth? You're not alone. According to the Planning Standards Council, over 60% of consumers feel their financial advisor puts their company's interests first. Only a staggering 12% believe their advisor is acting in their interests. From misconduct to hidden fees and commission deals, the problem has become so severe the federal government has recently acted to curb the impact on consumers and their financial security, but it doesn't go nearly far enough.</p>
  <p style="top:308px">VenholdRusk is focused on acting in your best interests. It's what we call Open Fiduciary and it's not only our promise, it's our very nature.</p>
  <div class="video">
    <div class="screen" role="img" aria-label="Explainer video still with a sketched advisor character"></div>
    <div class="play"></div>
    <div class="bar"><i></i></div>
  </div>
</section>

<section class="tiles">
  <div class="tile">
    <h3><svg width="22" height="18" viewBox="0 0 22 18"><path d="M1 1 V17 H21" stroke="#fff" stroke-width="2" fill="none"/><rect x="5" y="9" width="3" height="6" fill="#fff"/><rect x="10" y="5" width="3" height="10" fill="#fff"/><rect x="15" y="7" width="3" height="8" fill="#fff"/></svg>Fiduciary Principles</h3>
    <p>Sed ut perspiciatis unde omnis iste natus error sivolu ptatem accusantium doloremque laudantium</p>
  </div>
  <div class="tile">
    <h3><svg width="22" height="18" viewBox="0 0 22 18"><circle cx="7" cy="10" r="5" fill="none" stroke="#333" stroke-width="3"/><circle cx="17" cy="5" r="3" fill="none" stroke="#333" stroke-width="2"/></svg>Who We Serve</h3>
    <p>Sed ut perspiciatis unde omnis iste natus error sivolu ptatem accusantium doloremque laudantium</p>
  </div>
  <div class="tile">
    <h3><svg width="24" height="18" viewBox="0 0 24 18"><circle cx="7" cy="5" r="4" fill="#333"/><circle cx="17" cy="5" r="4" fill="#333"/><path d="M0 17 Q0 9 7 9 Q14 9 14 17 Z M10 17 Q10 9 17 9 Q24 9 24 17 Z" fill="#333"/></svg>Who We Are</h3>
    <p>Sed ut perspiciatis unde omnis iste natus error sivolu ptatem accusantium doloremque laudantium</p>
  </div>
  <div class="tile">
    <h3><svg width="24" height="18" viewBox="0 0 24 18"><rect x="1" y="1" width="22" height="16" fill="none" stroke="#333" stroke-width="2"/><rect x="4" y="4" width="7" height="6" fill="#333"/><path d="M13 5 H20 M13 9 H20 M4 13 H20" stroke="#333" stroke-width="1.5"/></svg>News and Media</h3>
    <p>Sed ut perspiciatis unde omnis iste natus error sivolu ptatem accusantium doloremque laudantium</p>
  </div>
</section>

<div class="press">
  <span>NBX</span><span>Castor</span><span>Tallmarket</span><span>BVR</span><span>Marlow</span><span>Capitolian</span><span>Ledgerline</span>
</div>

<footer class="footer">
  <div class="brand">
    <div class="brand-name"><i></i>VenholdRusk</div>
    <div class="brand-tag">Candid Family Wealth Partners</div>
  </div>
  <p class="about">Sed ut perspiciatis unde omnis iste turro tem accusantium doloremque laudantiperi am, eaque ipsa quae ab illo inventor vitaset quasi architecto beatae vitae dicta licabo.</p>
  <div class="fcol" style="left:418px">
    <h5>VenholdRusk</h5>
    4820 Linden Court<br>Suite 310<br>Halbrook, VA 20111<br>Office: (555) 014-2290<br>Toll free: 800-55-CLEAR<br>info@venholdrusk.com
  </div>
  <div class="fcol" style="left:616px">
    <h5>Help You</h5>
    Family Office<br>American Entrepreneurs<br>Insights<br>Terms of Use<br>Privacy Policy
  </div>
  <div class="fcol" style="left:785px">
    <h5>What We Do</h5>
    Sed ut perspiciatis<br>Qnde omnis iste n<br>Whus error sit voluptat<br>em accusantiu<br>Gdoloremque
  </div>
  <div class="fcol" style="left:965px">
    <h5>Company</h5>
    Company info<br>News<br>Investors<br>Sed ut perspeci<br>em accusantiu<br>Policies
  </div>
  <div class="baseline"></div>
  <div class="copy">© 2016. VenholdRusk All Copyrights are Reserved. Terms of Use &nbsp;&nbsp; Privacy Policy &nbsp;&nbsp; Sitemap</div>
  <div class="social">
    <i style="background:#2aa3e0"></i><i style="background:#2f58a8"></i><i style="background:#1c6fa6"></i><i style="background:#d9473b"></i>
  </div>
</footer>

</body>
</html>
```